Presentation for Design Industry

Halvorsen Custom Plastics & Acrylics is a custom plastic design/build company based in Canada that actively collaborates with Architects, Designers and Builders.
The versatility and economic attractiveness of plastics has engendered a renaissance in the use of this material in all aspects for our wide client base. We have changed our company from being a custom manufacturer. We are now embracing the opportunity to be part of the design process and contribute\ing unique design features using leading edge approaches and materials.
We would like our presentation to highlight this new design aspect of our company. One of our partners is www.lumevo-panels.example ~ this particular website outlines much of what we do and can be used as an example for design focussed towards our same target market. We are looking for a high-end, original presentation. If the design and concept is good, there are opportunities to be involved in our new website build within the next month.
A loose outline of our presentation is uploaded for your reference. Our brochures and graphics files are also available for your reference.
Adobe Acrobat Presentation*, PowerPoint or Google Presentation
http://halvorsenplastics.example/interior-industrial-design.htm
https://files.example-share.net/sh/kx4wd7mbt2h9r0n/Lmvq35zrea
Updates
Thank you to all who worked on submitting your designs based on a vague but necessary description. We were looking for something to pop out at us...not knowing exactly what we wanted we needed a design concept to emerge from the information we were able to provide. Perhaps this needed some entrepreneurial thought process or marketing experience behind the design concept. You all had great ideas. Thank you again for all your hard work and creativity!
Target Market(s)
Interior Designers; Architects; Environmental Designer, Building Contractors, Retail Designers
Industry/Entity Type
Plastic
Look and feel
Each slider illustrates characteristics of the customer's brand and the style your logo design should communicate.

```html
<!DOCTYPE html>
<html lang="en">
<head>
<meta charset="utf-8">
<title>The Team – John Doe</title>
<link rel="stylesheet" href="https://fonts.googleapis.com/css2?family=Questrial&display=swap">
<style>
  :root {
    --ink: #6b6b6b;
    --paper: #ffffff;
    --band: #a7dbe0;
    --band-text: #ffffff;
    --shirt-light: #dbe8f5;
    --shirt-mid: #b9d0ea;
    --skin: #e9c6ac;
  }
  html, body {
    margin: 0;
    padding: 0;
    overflow: hidden;
    background: var(--paper);
  }
  .slide {
    position: relative;
    width: 1200px;
    height: 676px;
    overflow: hidden;
    background: var(--paper);
    font-family: "Questrial", "Century Gothic", sans-serif;
    color: var(--ink);
  }
  .portrait {
    position: absolute;
    left: 640px;
    top: 0;
    width: 370px;
    height: 676px;
    border-radius: 150px 150px 0 0;
    background: linear-gradient(180deg, var(--skin) 0%, var(--skin) 28%, var(--shirt-light) 34%, var(--shirt-mid) 100%);
    opacity: 0.85;
  }
  .profile {
    position: absolute;
    left: 60px;
    top: 58px;
    width: 440px;
  }
  .profile__name {
    margin: 0;
    font-size: 57px;
    font-weight: 400;
    line-height: 1;
    letter-spacing: 0.5px;
  }
  .profile__role {
    margin: 8px 0 0;
    font-size: 26px;
    font-weight: 400;
    line-height: 1.2;
  }
  .profile__bio {
    margin: 22px 0 0;
    font-size: 16.5px;
    line-height: 24px;
  }
  .profile__bio + .profile__bio {
    margin-top: 24px;
  }
  .section-band {
    position: absolute;
    left: 0;
    top: 480px;
    width: 1200px;
    height: 118px;
    background: var(--band);
  }
  .section-band__title {
    position: absolute;
    left: 56px;
    top: 26px;
    margin: 0;
    font-size: 62px;
    font-weight: 400;
    line-height: 1;
    color: var(--band-text);
  }
  .brand {
    position: absolute;
    right: 30px;
    top: 47px;
    display: flex;
    align-items: center;
    gap: 8px;
    color: var(--band-text);
    font-size: 20px;
  }
  .brand__mark {
    width: 14px;
    height: 14px;
    background: var(--band-text);
  }
</style>
</head>
<body>
  <main class="slide">
    <div class="portrait" role="img" aria-label="Photo of team member John Doe in a light blue shirt, arms crossed"></div>

    <section class="profile">
      <h1 class="profile__name">John Doe</h1>
      <h2 class="profile__role">Industrial Designer</h2>
      <p class="profile__bio">This should be a short description of the tem<br>member, his professional experience and<br>expertese and possibly what makes him/her<br>a valuable asset to Halvorsen.</p>
      <p class="profile__bio">I think presenting each team memeber<br>individually creates sense of trustworthiness and<br>personally getting to know the person.</p>
    </section>

    <div class="section-band">
      <h2 class="section-band__title">The Team</h2>
      <div class="brand">
        <span class="brand__mark"></span>
        <span class="brand__name">Halvorsen</span>
      </div>
    </div>
  </main>
</body>
</html>
```